body balm label design

body balm tube design, current label design for other similar products
Need to have a design which can interchange between 3 different solutions
Amber Tide (Lavender + Vanilla)
Copper Harbor (Eucalyptus + Mint)
Velvet Arc (Bergamot + Cedarwood)
Tube size:
2.5h x 3.25 w
Target Market(s)
natural, solution focused
Requirements
Must have
- relatable to existing brand designs, focus on features and benefits

```html
<!DOCTYPE html>
<html lang="en">
<head>
<meta charset="utf-8">
<title>Body Balm Labels</title>
<link href="https://fonts.googleapis.com/css2?family=Playfair+Display:wght@900&family=Lato:wght@400;700&display=swap" rel="stylesheet">
<style>
  :root {
    --canvas: #ffffff;
    --lavender-bg: #e6e3f6;
    --lavender-ink: #4a2fa0;
    --lavender-soft: #b8acdf;
    --peach-bg: #f8d9c4;
    --peach-ink: #6e3519;
    --peach-soft: #e2ad8d;
    --sage-bg: #e9f3e1;
    --sage-ink: #2f5c43;
    --sage-soft: #b6ccb0;
  }
  * { margin: 0; padding: 0; box-sizing: border-box; }
  html, body { width: 1200px; height: 800px; overflow: hidden; background: var(--canvas); }
  .lineup {
    width: 1200px; height: 800px;
    display: flex; justify-content: space-between; align-items: center;
    padding: 0 56px;
  }
  .label {
    width: 318px; height: 560px;
    background: var(--bg);
    color: var(--ink);
    clip-path: polygon(0 0, 100% 0, 94% 100%, 6% 100%);
    display: flex; flex-direction: column; align-items: center;
    padding-top: 66px;
    text-align: center;
  }
  .label--amber  { --bg: var(--lavender-bg); --ink: var(--lavender-ink); --soft: var(--lavender-soft); }
  .label--velvet { --bg: var(--peach-bg);    --ink: var(--peach-ink);    --soft: var(--peach-soft); }
  .label--copper { --bg: var(--sage-bg);     --ink: var(--sage-ink);     --soft: var(--sage-soft); }
  .category {
    font-family: "Lato", sans-serif; font-weight: 400;
    font-size: 16px; letter-spacing: 0.2px;
  }
  .product-name {
    font-family: "Playfair Display", serif; font-weight: 900;
    font-size: 50px; line-height: 0.95; letter-spacing: -0.5px;
    margin-top: 22px; text-transform: uppercase;
  }
  .artwork {
    width: 120px; height: 140px; margin-top: 38px;
    border-radius: 50%;
    background: radial-gradient(circle, var(--soft) 0%, var(--bg) 72%);
  }
  .benefit {
    margin-top: 50px;
    display: flex; align-items: center; gap: 10px;
  }
  .benefit-mark {
    width: 10px; height: 10px; border-radius: 50%;
    border: 1.2px solid var(--ink);
  }
  .benefit-text {
    font-family: "Lato", sans-serif; font-weight: 400;
    font-size: 16px; line-height: 1.1; text-transform: uppercase;
  }
  .rule {
    width: 204px; height: 2px; background: var(--ink);
    margin-top: 10px;
  }
  .scent {
    font-family: "Lato", sans-serif; font-weight: 400;
    font-size: 16px; margin-top: 16px; text-transform: uppercase;
  }
</style>
</head>
<body>
<main class="lineup">

  <section class="label label--amber">
    <p class="category">BODY BALM</p>
    <h2 class="product-name">Amber<br>Tide</h2>
    <div class="artwork" role="img" aria-label="Line drawing of lavender sprigs with a small flower"></div>
    <div class="benefit">
      <span class="benefit-mark" role="img" aria-label="Small icon"></span>
      <p class="benefit-text">Naturally clam<br>mind &amp; body</p>
      <span class="benefit-mark" role="img" aria-label="Small icon"></span>
    </div>
    <div class="rule"></div>
    <p class="scent">Lavender + Vanilla</p>
  </section>

  <section class="label label--velvet">
    <p class="category">BODY BALM</p>
    <h2 class="product-name">Velvet<br>Arc</h2>
    <div class="artwork" role="img" aria-label="Line drawing of a whole and a halved bergamot fruit"></div>
    <div class="benefit">
      <span class="benefit-mark" role="img" aria-label="Small icon"></span>
      <p class="benefit-text">Naturally eases<br>tension &amp; anxiety</p>
      <span class="benefit-mark" role="img" aria-label="Small icon"></span>
    </div>
    <div class="rule"></div>
    <p class="scent">Bergamot + Cedarwood</p>
  </section>

  <section class="label label--copper">
    <p class="category">BODY BALM</p>
    <h2 class="product-name">Copper<br>Harbor</h2>
    <div class="artwork" role="img" aria-label="Line drawing of a mint leaf sprig"></div>
    <div class="benefit">
      <span class="benefit-mark" role="img" aria-label="Small icon"></span>
      <p class="benefit-text">Naturally smooth<br>achy muscles</p>
      <span class="benefit-mark" role="img" aria-label="Small icon"></span>
    </div>
    <div class="rule"></div>
    <p class="scent">Eucalyptus + Mint</p>
  </section>

</main>
</body>
</html>
```